Advert for Services that we offer

Bolt Remova Ltd need an design to represent what we do in a modern way by showing an image with a brief description and the use of corporate logo the information we will proved vie a doc file and this is to be presented in a modern way. This design will be for print & web. we have done our own design and its not great i have put this in the file repository

Target Market(s)

Motor trade

Font styles to use
Sans Serif

Colors

Designer to choose colors to be used in the design.

Requirements
Must have
• Company colour scheme as per logo within the files uploaded.
• and a small boarder to isolate it from the rest of the articles.
Nice to have
• Modern font
Should not have
• Old style font

```html
<!DOCTYPE html>
<html lang="en">
<head>
<meta charset="utf-8">
<title>Bolt Remova Ltd – Product Testing &amp; Analysis</title>
<link href="https://fonts.googleapis.com/css2?family=Montserrat:wght@400;500;700&display=swap" rel="stylesheet">
<style>
  :root {
    --page-bg: #e9ecef;
    --card-border: #ffffff;
    --panel-light: #f2f3f4;
    --panel-mid: #d9dbde;
    --brand-blue: #1466ae;
    --logo-blue: #2a86d0;
    --ink: #1b1c1e;
    --photo-light: #c9ccd0;
    --photo-dark: #2a2e35;
  }
  * { box-sizing: border-box; margin: 0; padding: 0; }
  html, body {
    width: 1200px; height: 875px; overflow: hidden;
    background: var(--page-bg);
    font-family: "Montserrat", Arial, sans-serif;
  }
  .advert {
    position: absolute; left: 50px; top: 82px;
    width: 1100px; height: 711px;
    background: var(--card-border);
    padding: 34px 37px;
    box-shadow: 0 6px 24px rgba(0,0,0,0.12);
  }
  .advert-panel {
    position: relative; width: 100%; height: 100%; overflow: hidden;
    background: linear-gradient(135deg, var(--panel-light) 0%, var(--panel-mid) 100%);
  }
  .hero-photo {
    position: absolute; top: 0; right: 0; width: 49%; height: 100%;
    background: linear-gradient(100deg, rgba(201,204,208,0) 0%, var(--photo-light) 12%, #6b6f76 45%, var(--photo-dark) 75%, #1f2228 100%);
  }
  .headline { position: absolute; left: 36px; top: 38px; line-height: 1.1; }
  .headline-top { font-size: 42px; font-weight: 400; color: var(--ink); letter-spacing: 0.5px; }
  .headline-main { font-size: 45px; font-weight: 700; color: var(--brand-blue); letter-spacing: 0.3px; }
  .service-list { position: absolute; left: 30px; top: 188px; list-style: none; }
  .service-item {
    display: flex; align-items: center; height: 59px;
    font-size: 33px; font-weight: 500; color: var(--ink);
  }
  .service-number {
    width: 35px; height: 35px; border-radius: 50%;
    background: var(--brand-blue); color: #fff;
    font-size: 23px; font-weight: 700;
    display: flex; align-items: center; justify-content: center;
    margin-right: 18px; flex-shrink: 0;
  }
  .contact { position: absolute; left: 36px; top: 512px; line-height: 1.15; }
  .contact-phone { font-size: 40px; font-weight: 700; color: var(--brand-blue); }
  .contact-web { font-size: 38px; font-weight: 700; color: var(--ink); }
  .brand-name {
    position: absolute; right: 30px; bottom: 44px;
    display: flex; align-items: center; gap: 10px;
    font-size: 22px; font-weight: 700; color: var(--logo-blue);
    text-transform: uppercase; letter-spacing: 0.5px;
  }
  .brand-mark { width: 16px; height: 16px; background: var(--logo-blue); }
</style>
</head>
<body>
  <section class="advert">
    <div class="advert-panel">
      <div class="hero-photo" role="img" aria-label="Technician in dark overalls measuring the bore of a flanged metal housing with a dial gauge"></div>

      <h1 class="headline">
        <span class="headline-top">PRODUCT</span><br>
        <span class="headline-main">TESTING &amp; ANALYSIS</span>
      </h1>

      <ol class="service-list">
        <li class="service-item"><span class="service-number">1</span>Metallurgical Testing</li>
        <li class="service-item"><span class="service-number">2</span>Bearing Pre-load Testing</li>
        <li class="service-item"><span class="service-number">3</span>Bore Measurement</li>
        <li class="service-item"><span class="service-number">4</span>New Product Evaluation</li>
        <li class="service-item"><span class="service-number">5</span>Product Analysis &amp; Report</li>
      </ol>

      <div class="contact">
        <p class="contact-phone">0161 555 0192</p>
        <p class="contact-web">www.bolt-remova.co.uk</p>
      </div>

      <div class="brand-name"><span class="brand-mark"></span>Bolt Remova Ltd</div>
    </div>
  </section>
</body>
</html>
```